Biz Card for Harrowfield Property Partners - HWPP

Harrowfield Property Partners is a commercial real estate acquisitions firm. We buy commercial property and need to raise capital from investors for each deal we buy. The vibe needs to be: give us your money, we will multiply it.
Our website: www.hrwpp-example.com
Competitors are: https://velmarholdings-example.com/, https://tribanquepartners-example.com/, http://www.ostrellecapital-example.com/
Target Market(s)
High Net Worth Individuals, Bankers, Insurance Companies, Commercial Real Estate Brokers.
Industry/Entity Type
Investment Banking
Contact Information for Business Card
Name, Title, Addess, Cell#, Office#, email, website
Requirements
Must have
- use one of our logos. See website for look and feel: www.hrwpp-example.com
Nice to have
- see website: www.hrwpp-example.com

```html
<!DOCTYPE html>
<html lang="en">
<head>
<meta charset="utf-8">
<title>Harrowfield Property Partners – Business Card</title>
<link href="https://fonts.googleapis.com/css2?family=Montserrat:wght@500&family=Poppins:wght@400;600;700&display=swap" rel="stylesheet">
<style>
  :root {
    --navy: #03243f;
    --navy-soft: rgba(255,255,255,0.08);
    --paper: #ffffff;
    --mist: #e9ecef;
    --stage: #1f2022;
    --ink: #03243f;
  }
  * { box-sizing: border-box; margin: 0; padding: 0; }
  html, body { width: 1200px; height: 1200px; overflow: hidden; }
  body {
    background: var(--stage);
    position: relative;
    font-family: "Poppins", sans-serif;
  }
  .card {
    position: absolute;
    left: 160px;
    width: 880px;
    height: 503px;
    overflow: hidden;
    box-shadow: 0 10px 30px rgba(0,0,0,0.5);
  }
  .card--back { top: 70px; background: var(--navy); }
  .card--front { top: 627px; background: var(--paper); }

  /* Back */
  .back-halo {
    position: absolute; left: -170px; top: -40px;
    width: 560px; height: 560px; border-radius: 50%;
    background: var(--navy-soft);
  }
  .back-brand {
    position: absolute; left: 300px; top: 110px; width: 520px;
    display: flex; flex-direction: column; align-items: center;
    color: var(--paper);
    font-family: "Montserrat", sans-serif; font-weight: 500;
  }
  .back-brand .brand-dot {
    width: 104px; height: 104px; border-radius: 50%;
    background: var(--paper); margin-bottom: 18px;
  }
  .brand-main { font-size: 44px; letter-spacing: 0.22em; line-height: 1; }
  .brand-sub { font-size: 15px; letter-spacing: 0.42em; margin-top: 10px; }
  .back-url {
    position: absolute; left: 300px; width: 520px; top: 400px;
    text-align: center; color: var(--paper);
    font-family: "Montserrat", sans-serif; font-weight: 500;
    font-size: 17px; letter-spacing: 0.45em;
  }

  /* Front */
  .front-band {
    position: absolute; left: 0; top: 0; bottom: 0; width: 170px;
    background: var(--navy);
  }
  .front-halo {
    position: absolute; left: 470px; top: 115px;
    width: 560px; height: 560px; border-radius: 50%;
    background: var(--mist);
  }
  .front-mark {
    position: absolute; left: 98px; top: 42px;
    width: 144px; height: 144px; border-radius: 50%;
    background: var(--navy); border: 6px solid var(--paper);
    box-shadow: 0 0 0 1px var(--navy);
  }
  .front-brand {
    position: absolute; left: 268px; top: 72px;
    color: var(--ink);
    font-family: "Montserrat", sans-serif; font-weight: 500;
  }
  .front-brand .brand-main { font-size: 50px; }
  .front-brand .brand-sub { font-size: 16px; margin-top: 12px; }

  .person { position: absolute; left: 240px; top: 268px; color: var(--ink); }
  .person-name { font-weight: 700; font-size: 26px; line-height: 1.1; letter-spacing: 0.02em; }
  .person-title { font-size: 19px; line-height: 1.2; }
  .divider {
    position: absolute; left: 230px; right: 40px; top: 336px;
    height: 2px; background: var(--ink);
  }
  .contact-list {
    position: absolute; left: 240px; top: 356px;
    list-style: none; color: var(--ink); font-size: 19px; line-height: 34px;
  }
  .contact-list li { display: flex; align-items: center; gap: 14px; }
  .contact-list svg { width: 22px; height: 22px; flex: none; }
  .address {
    position: absolute; right: 44px; top: 360px;
    text-align: right; color: var(--ink); font-size: 18px; line-height: 30px;
  }
</style>
</head>
<body>

<section class="card card--back" aria-label="Card back">
  <div class="back-halo"></div>
  <div class="back-brand">
    <div class="brand-dot"></div>
    <div class="brand-main">HARROWFIELD</div>
    <div class="brand-sub">PROPERTY PARTNERS</div>
  </div>
  <div class="back-url">www.hrwpp-example.com</div>
</section>

<section class="card card--front" aria-label="Card front">
  <div class="front-band"></div>
  <div class="front-halo"></div>
  <div class="front-mark"></div>
  <div class="front-brand">
    <div class="brand-main">HARROWFIELD</div>
    <div class="brand-sub">PROPERTY PARTNERS</div>
  </div>

  <div class="person">
    <div class="person-name">MARCUS T. ELLERY</div>
    <div class="person-title">Executive Director</div>
  </div>
  <div class="divider"></div>

  <ul class="contact-list">
    <li>
      <svg viewBox="0 0 24 24" aria-hidden="true"><circle cx="12" cy="12" r="12" fill="#03243f"/><path d="M9 6.5c.6 0 1.5 2.2 1.5 2.7s-1 .9-1 1.5c0 1 2.3 3.6 3.4 3.6.6 0 1-1 1.5-1s2.6 1 2.6 1.6c0 1.2-1.3 2.2-2.6 2.2C10.9 17.1 7 13 7 9.3 7 7.8 8.1 6.5 9 6.5z" fill="#fff"/></svg>
      <span>555-014-2738</span>
    </li>
    <li>
      <svg viewBox="0 0 24 24" aria-hidden="true"><circle cx="12" cy="12" r="12" fill="#03243f"/><rect x="8" y="5.5" width="8" height="13" rx="1.5" fill="#fff"/><rect x="9.3" y="7.3" width="5.4" height="8.4" fill="#03243f"/></svg>
      <span>555-019-6051</span>
    </li>
    <li>
      <svg viewBox="0 0 24 24" aria-hidden="true"><circle cx="12" cy="12" r="12" fill="#03243f"/><rect x="6" y="8" width="12" height="8.5" rx="1" fill="#fff"/><path d="M6.5 8.5l5.5 4.5 5.5-4.5" stroke="#03243f" stroke-width="1.2" fill="none"/></svg>
      <span>info@hrwpp-example.com</span>
    </li>
  </ul>

  <div class="address">
    PO Box 418 Quayside Row<br>
    2nd Street Harborton, USA<br>
    www.hrwpp-example.com
  </div>
</section>

</body>
</html>
```